PERMITRONICS: "THE CRAFT OF CREDENTIALS"

WE NEED A SIMPLE MODERN WEBSITE THAT EXPLAINS THE FIRM SERVICES OF HELPING PEOPLE WITH ALL THINGS RELATED TO FLORIDA STATE LICENSING IN THE USA (STATE LICENSES FOR BUILDERS AND ELECTRICIANS). WE HANDLE INIITIAL APPLICATION FOR LICENSURE, ADDITIONAL LICENSURE FOR THEIR SECOND OR THIRD COMPANIES, WE DEFEND PEOPLE WHO HAVE COMPLAINTS AGAINST THEIR LICENSE, HELP THEM WHILE ON LICENSE PROBATION, HELP THEM TERMINATE PROBATION, HELP THEM WITH CONTINUING EDUCATION SERVICES TO MAINTAIN THEIR LICENSE, AND WE HELP BROKER LICENSURE FOR PEOPLE LOOKING FOR A LICENSED PERSON TO LICENSE THEIR COMPANY.

```html
<!DOCTYPE html>
<html lang="en">
<head>
<meta charset="UTF-8">
<title>Permitronics – The Craft of Credentials</title>
<link href="https://fonts.googleapis.com/css2?family=Montserrat:wght@300;400;500;600;700&display=swap" rel="stylesheet">
<style>
  :root{
    --teal:#0fb3bd;
    --teal-dark:#0a9fb0;
    --blue:#0a8fd6;
    --green:#16c1a0;
    --hero-bg:#d4ecee;
    --services-bg:#e1f4fa;
    --ink:#111111;
    --text:#2b2b2b;
    --white:#ffffff;
    --footer:#000000;
    --rule:#4a4a4a;
  }
  *{margin:0;padding:0;box-sizing:border-box}
  html,body{width:1200px;height:3675px;overflow:hidden}
  body{font-family:"Montserrat",sans-serif;color:var(--text);background:var(--white);position:relative}
  .abs{position:absolute}
  .photo{position:absolute}

  /* header + hero */
  .hero{position:absolute;left:0;top:0;width:1200px;height:581px;background:var(--hero-bg);border-top:3px solid var(--teal)}
  .brand{position:absolute;left:98px;top:54px;display:flex;align-items:center;gap:10px;font-size:25px;font-weight:500;color:#555}
  .brand-dot{width:22px;height:22px;border-radius:50%;background:var(--teal)}
  .nav{position:absolute;top:42px;font-size:15.5px;color:#333;font-weight:400}
  .call-tab{position:absolute;left:899px;top:0;width:43px;height:86px;background:var(--teal);border-radius:0 0 22px 22px;display:flex;align-items:flex-end;justify-content:center;padding-bottom:8px}
  .call-tab span{width:31px;height:31px;border-radius:50%;background:var(--white);display:flex;align-items:center;justify-content:center}
  .call-label{position:absolute;left:955px;top:26px;font-size:17px;font-weight:600;color:var(--ink)}
  .call-number{position:absolute;left:960px;top:54px;font-size:17px;color:#333}
  .hero-welcome{position:absolute;left:98px;top:196px;font-size:40px;font-weight:300;color:var(--ink)}
  .hero-title{position:absolute;left:98px;top:242px;font-size:62px;font-weight:700;color:var(--ink);letter-spacing:.5px}
  .hero-text{position:absolute;left:98px;top:332px;width:440px;font-size:15.5px;line-height:25.7px;color:#333}
  .btn{position:absolute;display:flex;align-items:center;justify-content:center;gap:10px;border-radius:24px;font-size:16px;font-weight:600}
  .btn-teal{background:var(--teal-dark);color:var(--white)}
  .btn-white{background:var(--white);color:var(--teal-dark)}
  .arrow{width:14px;height:14px}

  /* about */
  .section-title{position:absolute;font-weight:700;color:var(--ink)}
  .title-dot{display:inline-block;width:26px;height:26px;border-radius:50%;border:3px solid var(--teal);vertical-align:middle;margin-left:18px}
  .about-text{position:absolute;left:645px;top:786px;width:450px;font-size:15.3px;line-height:25.7px;color:#333}
  .collage{border-radius:14px}

  /* services */
  .services{position:absolute;left:0;top:1270px;width:1200px;height:1144px;background:var(--services-bg)}
  .svc-title{position:absolute;font-size:26px;font-weight:700;color:var(--ink)}
  .svc-text{position:absolute;width:310px;font-size:15.3px;line-height:21.4px;color:#222}
  .svc-left{left:97px}
  .svc-right{left:792px}
  .right{text-align:right}

  /* mission */
  .mission-card{position:absolute;left:98px;top:2593px;width:491px;height:399px;border-radius:17px;background:linear-gradient(135deg,var(--green),var(--blue))}
  .mission-title{position:absolute;left:137px;top:2622px;font-size:40px;font-weight:700;color:var(--white)}
  .mission-title .title-dot{border-color:var(--white)}
  .mission-text{position:absolute;left:140px;top:2690px;width:400px;font-size:15.3px;line-height:30px;color:var(--white);font-weight:500}

  /* footer */
  .footer{position:absolute;left:0;top:3158px;width:1200px;height:517px;background:var(--footer);color:var(--white)}
  .footer-mark{position:absolute;left:560px;top:3250px;width:80px;height:80px;border-radius:50%;border:5px solid var(--teal)}
  .footer-brand{position:absolute;left:0;width:1200px;top:3340px;text-align:center;font-size:62px;font-weight:600;color:var(--white)}
  .footer-nav{position:absolute;top:3472px;font-size:22px;font-weight:600;color:var(--white)}
  .footer-rule{position:absolute;left:98px;top:3545px;width:1004px;height:2px;background:var(--rule)}
  .copyright{position:absolute;left:105px;top:3585px;font-size:17px;font-weight:500;color:var(--white)}
  .social{position:absolute;top:3577px;width:46px;height:46px;border-radius:50%;background:var(--teal-dark)}
</style>
</head>
<body>

<header class="hero">
  <div class="brand"><span class="brand-dot"></span>Permitronics</div>
  <a class="nav" style="left:464px">Home</a>
  <a class="nav" style="left:547px">About Us</a>
  <a class="nav" style="left:654px">Our Services</a>
  <a class="nav" style="left:785px">Contact Us</a>
  <div class="call-tab"><span>
    <svg width="14" height="14" viewBox="0 0 24 24"><path fill="#0fb3bd" d="M6.6 10.8a15 15 0 0 0 6.6 6.6l2.2-2.2a1 1 0 0 1 1-.25 11.4 11.4 0 0 0 3.6.57 1 1 0 0 1 1 1V20a1 1 0 0 1-1 1A17 17 0 0 1 3 4a1 1 0 0 1 1-1h3.5a1 1 0 0 1 1 1c0 1.25.2 2.45.57 3.57a1 1 0 0 1-.25 1z"/></svg>
  </span></div>
  <div class="call-label">Call Us</div>
  <div class="call-number">+1 555-014-2290</div>

  <div class="hero-welcome">Welcome to</div>
  <h1 class="hero-title">Permitronics</h1>
  <p class="hero-text">Florida state licensing help for builders and electricians, from your first application to every renewal after.</p>
  <a class="btn btn-teal" style="left:98px;top:408px;width:169px;height:46px">Get Started
    <svg class="arrow" viewBox="0 0 16 16"><circle cx="8" cy="8" r="8" fill="#fff"/><path d="M5 8h5M8 5l3 3-3 3" stroke="#0a9fb0" stroke-width="2" fill="none"/></svg></a>

  <div class="photo" role="img" aria-label="Smiling construction worker in a yellow hard hat and safety vest with arms crossed" style="left:606px;top:121px;width:379px;height:457px;background:linear-gradient(180deg,#b8dfe2 0%,#e8c36a 45%,#d9dde3 100%);border-radius:190px 190px 0 0"></div>
</header>

<section>
  <div class="photo collage" role="img" aria-label="Electrician working on a control panel" style="left:167px;top:691px;width:164px;height:218px;background:linear-gradient(160deg,#d7dbe0,#8c9aa6)"></div>
  <div class="photo collage" role="img" aria-label="Business meeting around an architectural model" style="left:345px;top:763px;width:193px;height:194px;background:linear-gradient(160deg,#b9885a,#4a3020)"></div>
  <div class="photo collage" role="img" aria-label="Construction workers viewing a building site at sunset" style="left:114px;top:922px;width:217px;height:254px;background:linear-gradient(170deg,#e9c58c,#7a5a3c 60%,#2e2a2a)"></div>
  <div class="photo collage" role="img" aria-label="Person holding a tablet displaying a license agreement" style="left:345px;top:979px;width:155px;height:164px;background:linear-gradient(160deg,#2c3a4f,#101820)"></div>

  <h2 class="section-title" style="left:645px;top:712px;font-size:38px">About Us<span class="title-dot"></span></h2>
  <p class="about-text">Permitronics helps Florida builders and electricians with every part of their state license. We prepare and file your initial application for licensure, add licenses for your second or third company, and stand beside you when a complaint is filed against your license. If you are on probation, we guide you through each condition and help you end it early where the rules allow. We also arrange the continuing education you need to keep your license active, and we broker licensure for firms looking for a qualified licensed person.</p>
  <a class="btn btn-teal" style="left:645px;top:1077px;width:167px;height:45px">Read More
    <svg class="arrow" viewBox="0 0 16 16"><circle cx="8" cy="8" r="8" fill="#fff"/><path d="M5 8h5M8 5l3 3-3 3" stroke="#0a9fb0" stroke-width="2" fill="none"/></svg></a>
</section>

<section class="services"></section>
<span class="abs" style="left:584px;top:1322px;width:32px;height:32px;border-radius:50%;border:3px solid var(--teal)"></span>
<h2 class="section-title" style="left:0;width:1200px;text-align:center;top:1373px;font-size:40px">Our Services</h2>

<svg class="abs" style="left:400px;top:1488px" width="400" height="400" viewBox="0 0 400 400">
  <circle cx="200" cy="200" r="178" fill="none" stroke="#b9c6cc" stroke-width="2" stroke-dasharray="8 7"/>
  <circle cx="200" cy="200" r="130" fill="#fff"/>
  <circle cx="200" cy="200" r="44" fill="none" stroke="#0fb3bd" stroke-width="8"/>
  <g fill="#fff" stroke="#cfe3ea">
    <circle cx="88" cy="53" r="34"/><circle cx="311" cy="53" r="34"/>
    <circle cx="88" cy="344" r="34"/><circle cx="311" cy="344" r="34"/>
  </g>
  <g fill="none" stroke="#222" stroke-width="2">
    <rect x="75" y="38" width="22" height="28" rx="2"/><path d="M80 46h12M80 52h12M80 58h8"/><circle cx="99" cy="62" r="5"/>
    <path d="M311 35l14 5v10c0 9-6 15-14 18-8-3-14-9-14-18V40z"/><circle cx="320" cy="64" r="6"/><path d="M317 64l2 2 4-4"/>
    <rect x="76" y="328" width="24" height="32" rx="2"/><path d="M81 336h14M81 342h14"/><circle cx="88" cy="352" r="4"/>
    <path d="M300 330h18v26h-20a4 4 0 0 1 0-8h14"/><path d="M306 336l5 2v4c0 3-2 5-5 6-3-1-5-3-5-6v-4z"/>
  </g>
</svg>

<h3 class="svc-title right svc-left" style="width:310px;top:1502px">Initial Licensure</h3>
<p class="svc-text right svc-left" style="top:1550px">We prepare and file your first Florida state application as a builder or electrician, and add licenses for a second or third company.</p>
<h3 class="svc-title svc-right" style="top:1502px">Complaint Defense</h3>
<p class="svc-text svc-right" style="top:1550px">When a complaint is filed against your license, we build your response and defend you through every step of the state process.</p>
<h3 class="svc-title right svc-left" style="width:310px;top:1747px">Probation Support</h3>
<p class="svc-text right svc-left" style="top:1795px">We help you meet each probation condition on time and work to terminate probation as early as the board allows.</p>
<h3 class="svc-title svc-right" style="top:1747px">Education &amp; Brokering</h3>
<p class="svc-text svc-right" style="top:1795px">We arrange continuing education to keep your license active, and match companies with a licensed person to qualify them.</p>

<div class="photo" role="img" aria-label="Group of smiling construction workers in hard hats and high-visibility vests" style="left:0;top:1940px;width:1200px;height:474px;background:linear-gradient(180deg,#e1f4fa 0%,#e9a23a 22%,#c9652e 55%,#3c5574 100%)"></div>

<section>
  <div class="photo" role="img" aria-label="Construction team reviewing a clipboard and laptop on site" style="left:488px;top:2531px;width:611px;height:524px;border-radius:17px;background:linear-gradient(160deg,#8a8a84,#c9c27a 45%,#5d6a4f)"></div>
  <div class="mission-card"></div>
  <h2 class="mission-title">Our Mission<span class="title-dot"></span></h2>
  <p class="mission-text">Our mission is to keep Florida builders and electricians licensed, compliant and working. We make state licensing simple, defend your record when it is questioned, and support you through probation and renewals, so you can spend your time on the job site instead of on paperwork.</p>
  <a class="btn btn-white" style="left:137px;top:2904px;width:167px;height:44px">Read More
    <svg class="arrow" viewBox="0 0 16 16"><circle cx="8" cy="8" r="8" fill="#0a9fb0"/><path d="M5 8h5M8 5l3 3-3 3" stroke="#fff" stroke-width="2" fill="none"/></svg></a>
</section>

<footer class="footer"></footer>
<span class="footer-mark"></span>
<div class="footer-brand">Permitronics</div>
<a class="footer-nav" style="left:305px">Home</a>
<a class="footer-nav" style="left:425px">About Us</a>
<a class="footer-nav" style="left:581px">Our Services</a>
<a class="footer-nav" style="left:773px">Contact Us</a>
<div class="footer-rule"></div>
<p class="copyright">Copyright © 2023 Permitronics - All Rights Reserved.</p>
<span class="social" style="left:996px" aria-label="Social link"></span>
<span class="social" style="left:1053px" aria-label="Social link"></span>

</body>
</html>
```